Quartz Meridian Business Card Design

I need a 2-sided business card for my computer engineering consulting company. The card is expected to convey a message of cutting edge forward thinking, and boldnes. I would like the card to be memorable and stand-out on a desk. The card should be bold, modern, clean, and highly professional. I am a big fan of watermarks/shadows and other intersting but restrained uses of the logo. The card can be a shape other than the traditional rectangle. Perhaps a rectangle with rounded edges. All I ask is the card be able to fit into a standard wallet. I will supply two logos, one with a red background, and one with a black background. Please feel free to work with both of these logos.
Updates

Hi all, thank you for your submissions. I will post the original vector file later today. Thank you for your patience.

Regards,

Henry

Target Market(s)

Engineering Buyers, Vice Presidents and Directors

Industry/Entity Type

Computer

Requirements
Must have
• 2 sides

```html
<!DOCTYPE html>
<html lang="en">
<head>
<meta charset="utf-8">
<title>Quartz Meridian Works LTD – Business Card</title>
<link rel="stylesheet" href="https://fonts.googleapis.com/css2?family=Open+Sans:wght@400;600&display=swap">
<style>
  :root {
    --page-bg: #ebebeb;
    --card-base: #1c1c1c;
    --card-light: #2a2a2a;
    --card-dark: #121212;
    --accent-red: #e8373d;
    --text-light: #e6e6e6;
    --text-muted: #b9b9b9;
    --text-font: "Open Sans", Arial, sans-serif;
  }
  * { margin: 0; padding: 0; box-sizing: border-box; }
  html, body {
    width: 1200px; height: 534px; overflow: hidden;
    background: var(--page-bg);
    font-family: var(--text-font);
  }
  .canvas { position: relative; width: 1200px; height: 534px; }

  .card {
    position: absolute; top: 119px;
    width: 525px; height: 299px;
    border-radius: 22px;
    background:
      radial-gradient(ellipse at 55% 35%, var(--card-light) 0%, var(--card-base) 55%, var(--card-dark) 100%);
    color: var(--text-light);
    overflow: hidden;
  }
  .card--front { left: 62px; }
  .card--back { left: 621px; }

  .brand-mark {
    position: absolute;
    background: var(--accent-red);
  }
  .card--front .brand-mark { left: 214px; top: 79px; width: 90px; height: 88px; }
  .card--back .brand-mark { left: 128px; top: 41px; width: 52px; height: 52px; }

  .brand-name {
    position: absolute; left: 0; right: 0; text-align: center;
    font-weight: 400; color: var(--accent-red);
    white-space: nowrap; letter-spacing: 0.5px;
  }
  .card--front .brand-name { top: 172px; font-size: 27px; }
  .card--back .brand-name { top: 96px; left: 48px; right: auto; font-size: 17px; }

  .tagline {
    position: absolute; left: 0; right: 0; text-align: center;
    color: var(--text-muted); letter-spacing: 3px; white-space: nowrap;
  }
  .card--front .tagline { top: 205px; font-size: 15px; }
  .card--back .tagline { top: 116px; left: 78px; right: auto; font-size: 9px; letter-spacing: 1.6px; }

  .website { color: var(--text-light); }
  .website .highlight { color: var(--accent-red); }
  .card--front .website {
    position: absolute; left: 0; right: 0; top: 254px;
    text-align: center; font-size: 13px;
  }

  .person { position: absolute; left: 48px; top: 160px; }
  .person__name { font-size: 18px; font-weight: 400; letter-spacing: 0.5px; }
  .person__name .first { color: var(--accent-red); }
  .person__role { font-size: 10px; color: var(--text-muted); margin-top: 1px; }

  .company { position: absolute; left: 48px; top: 212px; font-size: 10px; line-height: 13px; color: var(--text-muted); }
  .company__name { font-size: 12px; color: var(--text-light); margin-bottom: 4px; }
  .company__name .highlight { color: var(--accent-red); }

  .contact-list {
    position: absolute; left: 231px; top: 210px;
    list-style: none; font-size: 10px; line-height: 12.5px; color: var(--text-light);
  }
  .contact-list .label { color: var(--accent-red); }
</style>
</head>
<body>
<main class="canvas">

  <section class="card card--front" aria-label="Card front">
    <div class="brand-mark" aria-hidden="true"></div>
    <h1 class="brand-name">QUARTZ MERIDIAN WORKS LTD</h1>
    <p class="tagline">IMPOSSIBLE MADE POSSIBLE</p>
    <p class="website">www.<span class="highlight">Quartz</span>MeridianWorksLTD.com</p>
  </section>

  <section class="card card--back" aria-label="Card back">
    <div class="brand-mark" aria-hidden="true"></div>
    <h2 class="brand-name">QUARTZ MERIDIAN WORKS LTD</h2>
    <p class="tagline">IMPOSSIBLE MADE POSSIBLE</p>

    <div class="person">
      <p class="person__name"><span class="first">John</span> Doe</p>
      <p class="person__role">Position</p>
    </div>

    <address class="company" style="font-style:normal">
      <p class="company__name"><span class="highlight">Quartz</span> Meridian Works LTD</p>
      <p>000 Fifth Avenue, 00th Floor</p>
      <p>New York, NY 00000</p>
    </address>

    <ul class="contact-list">
      <li><span class="label">p:</span> + 12 111 22 77 62 11</li>
      <li><span class="label">m:</span> + 12 111 22 77 62 12</li>
      <li><span class="label">e:</span> info@quartzmeridianworksltd.com</li>
      <li class="website">www.<span class="highlight">Quartz</span>MeridianWorksLTD.com</li>
    </ul>
  </section>

</main>
</body>
</html>
```